One Page Template Mobile Reviews

Move our reviews web site template to a mobile template.
We produce a review web site for our customers like this one:

http://dental.brindlequeue.net/surveys57461/KoT31WQZ/surveys.htm

These are X pages with the exact same format.
We need to have this format adapted to an iPhone format.

So this is really ONE page project!

Target Market(s)

Patients looking for feedback on a particular practice

Industry/Entity Type

Dental

Requirements
Must have
• Running on iPhone using the HTML "viewport" tags

```html
<!DOCTYPE html>
<html lang="en">
<head>
<meta charset="utf-8">
<meta name="viewport" content="width=device-width, initial-scale=1">
<title>BrindleQueue – Patient Reviews</title>
<link rel="stylesheet" href="https://fonts.googleapis.com/css2?family=Open+Sans:ital,wght@0,400;0,600;0,700;1,400&display=swap">
<style>
  :root{
    --page-bg:#ececec;
    --screen-bg:#e9e9e9;
    --white:#ffffff;
    --brand-red:#8c1c1c;
    --brand-blue:#5a5acb;
    --doctor-green:#4c8a1e;
    --text:#3a3a3a;
    --muted:#6a6a6a;
    --link:#3b4fc4;
    --band:#5d9aa0;
    --review-text:#4e7c82;
    --star:#f2c315;
    --star-edge:#c99a05;
    --scroll-track:#d4d4d4;
    --scroll-thumb:#8e1e1e;
    --line:#d2d2d2;
    --map-base:#e6e1d6;
    --map-road:#f3e27a;
  }
  *{box-sizing:border-box;margin:0;padding:0}
  html,body{width:1200px;height:1080px;overflow:hidden}
  body{background:var(--page-bg);font-family:"Open Sans",sans-serif;color:var(--text)}
  .screen{position:absolute;left:300px;top:30px;width:600px;height:1020px;background:var(--screen-bg);overflow:hidden;box-shadow:0 0 0 1px #d0d0d0}

  .site-header{height:92px;background:var(--white);border-bottom:2px solid var(--line);display:flex;justify-content:space-between;align-items:flex-end;padding:0 22px 18px 22px}
  .brand{display:flex;align-items:center;gap:8px;font-size:34px;color:var(--brand-red);font-weight:400;letter-spacing:-.5px}
  .brand-dot{width:12px;height:12px;border-radius:50%;background:var(--brand-blue)}
  .header-info{text-align:right;font-size:15px;font-weight:600;color:var(--muted)}
  .header-info .phone{font-style:italic;margin-bottom:14px}
  .header-info .phone span{color:var(--brand-red)}

  .content{position:absolute;left:0;top:94px;width:576px;bottom:0}
  .scrollbar{position:absolute;right:0;top:94px;width:24px;bottom:0;background:var(--scroll-track)}
  .scrollbar .thumb{position:absolute;left:6px;top:8px;width:11px;height:120px;border-radius:6px;background:var(--scroll-thumb)}

  .profile{background:var(--white);height:144px;position:relative;padding:16px 20px;display:flex;gap:16px}
  .photo{width:80px;height:80px;background:linear-gradient(160deg,#6f86a8,#2d3a52);border:1px solid #999;flex:none}
  .doc-name{color:var(--doctor-green);font-size:17px;font-weight:600}
  .rating-row{font-size:14px;margin-top:4px}
  .rating-row .pct{color:var(--brand-red);font-weight:600;margin-right:10px}
  .rating-row .count{color:var(--muted)}
  .site-link{color:var(--link);font-size:13px}
  .address{font-style:italic;font-size:12.5px;line-height:19px}
  .page-no{position:absolute;right:14px;top:12px;font-size:13px}
  .page-no b{color:var(--brand-red)}

  .details{display:flex;gap:12px;padding:10px 14px 8px 22px;height:226px}
  .hours{width:243px;height:156px;background:var(--white);border:1px solid var(--line);padding:10px 10px}
  .panel-title{text-align:center;color:var(--brand-blue);font-size:14.5px;font-weight:600;margin-bottom:14px}
  .hours table{width:100%;font-size:13.5px;border-collapse:collapse}
  .hours td{padding:3px 0 4px}
  .hours td:last-child{text-align:right;font-size:13px}
  .map-panel{width:282px;height:212px;background:var(--white);border:1px solid var(--line)}
  .map-panel .panel-title{margin:12px 0 6px}
  .map-area{height:172px;background:linear-gradient(135deg,var(--map-base),#ddd6c7 60%,var(--map-road) 140%)}

  .reviews-band{margin:0 6px 0 32px;height:34px;background:var(--band);color:var(--white);font-size:14.5px;display:flex;align-items:center;justify-content:center;letter-spacing:.2px}
  .band-sub{text-align:center;font-size:13.5px;padding:10px 0 12px}

  .review{background:linear-gradient(#f8f8f8,#e6e6e6);height:174px;margin-bottom:8px;position:relative;padding:14px 20px 0 44px;display:flex;gap:14px}
  .reviewer{width:88px;text-align:center;font-size:12.5px;line-height:16px;flex:none}
  .avatar{width:88px;height:82px;background:var(--white);border:1px solid var(--line);margin-bottom:4px;display:flex;align-items:center;justify-content:center}
  .avatar div{width:52px;height:56px;background:linear-gradient(#d9bf8a,#9a9fa6);border-radius:26px 26px 4px 4px}
  .review-body{flex:1}
  .review-rating{display:flex;align-items:center;gap:6px;font-size:15px;color:var(--muted);font-weight:600}
  .dropdown{width:16px;height:14px;border:1px solid #9ab;background:#dde8f4;display:inline-block;position:relative}
  .dropdown:after{content:"";position:absolute;left:4px;top:4px;border:4px solid transparent;border-top:5px solid #3d5f8f}
  .review-title{color:var(--brand-red);font-weight:600;font-size:15.5px;margin-top:6px}
  .review-date{color:var(--review-text);font-style:italic;font-size:13px;margin-top:6px}
  .review-text{color:var(--review-text);font-style:italic;font-size:13px;line-height:22px}
  .review-index{position:absolute;right:20px;top:14px;font-size:13px;color:var(--muted)}
  .review-index b{color:var(--text)}
  .stars{display:inline-flex;gap:3px;vertical-align:middle}
</style>
</head>
<body>
<svg width="0" height="0" style="position:absolute" aria-hidden="true">
  <defs>
    <symbol id="star" viewBox="0 0 24 24"><path d="M12 1.8l3 6.6 7.2.8-5.4 4.9 1.5 7.1L12 17.6l-6.3 3.6 1.5-7.1L1.8 9.2 9 8.4z" fill="var(--star)" stroke="var(--star-edge)" stroke-width="1"/></symbol>
    <linearGradient id="half"><stop offset="50%" stop-color="#f2c315"/><stop offset="50%" stop-color="#ffffff"/></linearGradient>
    <symbol id="star-half" viewBox="0 0 24 24"><path d="M12 1.8l3 6.6 7.2.8-5.4 4.9 1.5 7.1L12 17.6l-6.3 3.6 1.5-7.1L1.8 9.2 9 8.4z" fill="url(#half)" stroke="var(--star-edge)" stroke-width="1"/></symbol>
  </defs>
</svg>

<main class="screen">
  <header class="site-header">
    <div class="brand"><span class="brand-dot"></span>BrindleQueue</div>
    <div class="header-info">
      <div class="phone">Phone: <span>(703) 555-0148</span></div>
      <div>Reviews From Verified Patients Only</div>
    </div>
  </header>

  <div class="content">
    <section class="profile">
      <div class="photo" role="img" aria-label="Portrait photo of the dentist"></div>
      <div>
        <div class="doc-name">Martin Ostrander DDS, FAGD</div>
        <span class="stars">
          <svg width="17" height="17"><use href="#star"/></svg><svg width="17" height="17"><use href="#star"/></svg><svg width="17" height="17"><use href="#star"/></svg><svg width="17" height="17"><use href="#star"/></svg><svg width="17" height="17"><use href="#star-half"/></svg>
        </span>
        <div class="rating-row"><span class="pct">98.19 %</span><span class="count">747 Reviews &amp; Surveys</span></div>
        <div class="site-link">www.drostrander.com</div>
        <div class="address">4810 Birchmont Lane Suite 120<br>Alderton, VA 22190</div>
      </div>
      <div class="page-no">Page <b>1</b> / 30</div>
    </section>

    <section class="details">
      <div class="hours">
        <div class="panel-title">OFFICE HOURS</div>
        <table>
          <tr><td>Monday</td><td>7:30 AM 2:00 PM</td></tr>
          <tr><td>Tuesday</td><td>7:30 AM 5:00 PM</td></tr>
          <tr><td>Wednesday</td><td>7:30 AM 5:00 PM</td></tr>
          <tr><td>Thursday</td><td>7:30 AM 1:00 PM</td></tr>
        </table>
      </div>
      <div class="map-panel">
        <div class="panel-title">OFFICE HOURS</div>
        <div class="map-area" role="img" aria-label="Street map showing the office location"></div>
      </div>
    </section>

    <div class="reviews-band">747 Certified Patients Reviews &amp; Surveys for Martin Ostrander DDS, FAGD</div>
    <div class="band-sub">Reviews posted and surveys rated from actual patients. Certified</div>

    <article class="review">
      <div class="reviewer"><div class="avatar" role="img" aria-label="Generic reviewer avatar"><div></div></div>LinaR<br>Fairbrook</div>
      <div class="review-body">
        <div class="review-rating"><span class="stars"><svg width="21" height="21"><use href="#star"/></svg><svg width="21" height="21"><use href="#star"/></svg><svg width="21" height="21"><use href="#star"/></svg><svg width="21" height="21"><use href="#star"/></svg><svg width="21" height="21"><use href="#star-half"/></svg></span>100.00 % <span class="dropdown"></span></div>
        <div class="review-title">I am especially grateful that ...</div>
        <div class="review-date">October 05, 2012</div>
        <p class="review-text">&nbsp;am especially grateful that Dr. Ostrander saw and immediately fixed a cavity that would have been a root canal if it had been left for a future appointment.</p>
      </div>
      <div class="review-index">Review(743): <b>1</b> /747</div>
    </article>

    <article class="review">
      <div class="reviewer"><div class="avatar" role="img" aria-label="Generic reviewer avatar"><div></div></div>LinaR<br>Fairbrook</div>
      <div class="review-body">
        <div class="review-rating"><span class="stars"><svg width="21" height="21"><use href="#star"/></svg><svg width="21" height="21"><use href="#star"/></svg><svg width="21" height="21"><use href="#star"/></svg><svg width="21" height="21"><use href="#star"/></svg><svg width="21" height="21"><use href="#star-half"/></svg></span>100.00 % <span class="dropdown"></span></div>
        <div class="review-title">I am especially grateful that ...</div>
        <div class="review-date">October 05, 2012</div>
        <p class="review-text">&nbsp;am especially grateful that Dr. Ostrander saw and immediately fixed a cavity that would have been a root canal if it had been left for a future appointment.</p>
      </div>
      <div class="review-index">Review(743): <b>1</b> /747</div>
    </article>

    <article class="review">
      <div class="reviewer"><div class="avatar" role="img" aria-label="Generic reviewer avatar"><div></div></div>LinaR<br>Fairbrook</div>
      <div class="review-body">
        <div class="review-rating"><span class="stars"><svg width="21" height="21"><use href="#star"/></svg><svg width="21" height="21"><use href="#star"/></svg><svg width="21" height="21"><use href="#star"/></svg><svg width="21" height="21"><use href="#star"/></svg><svg width="21" height="21"><use href="#star-half"/></svg></span>100.00 % <span class="dropdown"></span></div>
        <div class="review-title">I am especially grateful that ...</div>
        <div class="review-date">October 05, 2012</div>
        <p class="review-text">&nbsp;am especially grateful that Dr. Ostrander saw and immediately fixed a cavity that would have been a root canal if it had been left for a future appointment.</p>
      </div>
      <div class="review-index">Review(743): <b>1</b> /747</div>
    </article>
  </div>

  <div class="scrollbar"><div class="thumb"></div></div>
</main>
</body>
</html>
```